Flyer-Design für tamilisches Restaurant
Zielgruppe
Tamilisches Essen (kottu Rotti)
Aufgabenstellung
brauche eine zwei seitige A5 Flyer hoch oder quer spielt keine rolle das Hintergrund sollte Schwarz sein und paar Details in Gold wie unser Logo, das ist unsere Gedanke an design.
Auf der Vorderseite sollte, Neueröffnung am 01. März 2019 unser Hauptlogo, Facebook/ Instagram Logo in Gold mit unserer Seite (Selvo_Restaurant) und unser Motto #allaboutthebowl sein.
Auf der Rückseite, ein Bild mit kurzem Beschrieb ( Kottu Rotti das populärstes Gericht aus SriLanka)
Alle Gerichte zum mitnehmen und ab 8. März 2019 mit Lieferung.
unsere Öffnungszeiten
Montag bis Donnerstag 17.00 – 23.00 Uhr
Freitag 17.00 – 02.00 Uhr
Samstag 17.00 – 02.00 Uhr
Sonntag 17.00 – 23.00 Uhr
das Team von der Selvo freut such auf Ihren Besuch
Reservierungen unter 031 574 19 86
und noch unser Logo in klein Format

```html
<!DOCTYPE html>
<html lang="de">
<head>
<meta charset="utf-8">
<title>Selvo – Neueröffnung Flyer</title>
<link rel="stylesheet" href="https://fonts.googleapis.com/css2?family=Roboto+Slab:wght@300;400&family=Roboto:wght@400;700&display=swap">
<style>
  :root {
    --page: #ffffff;
    --flyer: #000000;
    --gold: #cdb47a;
    --gold-soft: #bfa76c;
  }
  * { margin: 0; padding: 0; box-sizing: border-box; }
  html, body { width: 1200px; height: 1189px; overflow: hidden; background: var(--page); }
  .canvas { position: relative; width: 1200px; height: 1189px; }

  .flyer {
    position: absolute;
    width: 460px;
    height: 650px;
    background: var(--flyer);
    color: var(--gold);
    font-family: "Roboto", sans-serif;
  }
  .flyer--front { left: 130px; top: 60px; }
  .flyer--back { left: 610px; top: 440px; overflow: hidden; }

  /* Front */
  .brand-mark {
    position: absolute;
    left: 50%;
    top: 70px;
    transform: translateX(-50%);
    width: 132px;
    height: 132px;
    border: 2px solid var(--gold);
    border-radius: 50%;
    display: flex;
    align-items: center;
    justify-content: center;
  }
  .brand-mark__name {
    font-family: "Roboto Slab", serif;
    font-weight: 400;
    font-size: 30px;
    letter-spacing: 1px;
    color: var(--gold);
  }
  .headline {
    position: absolute;
    top: 262px;
    width: 100%;
    text-align: center;
    font-family: "Roboto Slab", serif;
    font-weight: 300;
    font-size: 40px;
    letter-spacing: 1px;
  }
  .headline-rule {
    position: absolute;
    top: 326px;
    left: 50%;
    width: 70px;
    margin-left: -35px;
    border-top: 1.5px solid var(--gold);
  }
  .opening-date {
    position: absolute;
    top: 340px;
    width: 100%;
    text-align: center;
    font-size: 20px;
    letter-spacing: 0.5px;
  }
  .contact {
    position: absolute;
    top: 520px;
    width: 100%;
    text-align: center;
    font-size: 16px;
    line-height: 1.3;
  }
  .social {
    position: absolute;
    top: 584px;
    width: 100%;
    text-align: center;
    font-size: 17px;
  }

  /* Back */
  .back-text { position: absolute; left: 50px; top: 56px; right: 30px; }
  .intro { font-size: 12.5px; line-height: 1.3; }
  .hours-title {
    margin-top: 20px;
    font-family: "Roboto Slab", serif;
    font-weight: 300;
    font-size: 21px;
    letter-spacing: 0.5px;
  }
  .hours { list-style: none; margin-top: 4px; font-size: 12.5px; line-height: 1.28; }
  .greeting { margin-top: 16px; font-size: 12.5px; }
  .reservation { margin-top: 14px; font-size: 13px; font-weight: 700; display: flex; align-items: center; gap: 4px; }
  .reservation svg { width: 11px; height: 11px; fill: var(--gold); }
  .dish-caption {
    position: absolute;
    right: 36px;
    top: 356px;
    text-align: right;
    font-size: 12.5px;
    line-height: 1.3;
  }
  .dish-photo {
    position: absolute;
    left: 0;
    right: 0;
    bottom: 0;
    height: 250px;
    background:
      radial-gradient(ellipse 42% 48% at 46% 52%, #c8672b 0%, #b4541f 55%, rgba(180,84,31,0) 100%),
      radial-gradient(ellipse 18% 26% at 75% 40%, #f2d24f 0%, rgba(242,210,79,0) 100%),
      linear-gradient(180deg, #000 0%, #000 18%, #f4f1ec 38%, #ffffff 100%);
  }
</style>
</head>
<body>
<main class="canvas">

  <section class="flyer flyer--front" aria-label="Vorderseite">
    <div class="brand-mark"><span class="brand-mark__name">Selvo</span></div>
    <h1 class="headline">NEUERÖFFNUNG</h1>
    <div class="headline-rule"></div>
    <p class="opening-date">AM 01. MÄRZ 2019</p>
    <p class="contact">Mühlerainweg 7b | 4538 Oberfeldach<br>Tel.031 574 19 86</p>
    <p class="social">Selvo_Restaurant | #allaboutthebowl</p>
  </section>

  <section class="flyer flyer--back" aria-label="Rückseite">
    <div class="back-text">
      <p class="intro">Alle Gerichte zum mitnehmen und<br>ab 8. März 2019 mit Lieferung.</p>
      <h2 class="hours-title">UNSERE ÖFFNUNGSZEITEN</h2>
      <ul class="hours">
        <li>Montag – Donnerstag: 17.00 – 23.00 Uhr</li>
        <li>Freitag: 17.00 – 02.00 Uhr</li>
        <li>Samstag: 17.00 – 02.00 Uhr</li>
        <li>Sonntag: 17.00 – 23.00 Uhr</li>
      </ul>
      <p class="greeting">Das Team von der Selvo freut such auf Ihren Besuch.</p>
      <p class="reservation">Reservierungen unter
        <svg viewBox="0 0 24 24" aria-hidden="true"><path d="M6.6 10.8a15.1 15.1 0 0 0 6.6 6.6l2.2-2.2c.3-.3.7-.4 1-.2 1.1.4 2.3.6 3.6.6.6 0 1 .4 1 1V20c0 .6-.4 1-1 1A17 17 0 0 1 3 4c0-.6.4-1 1-1h3.5c.6 0 1 .4 1 1 0 1.3.2 2.5.6 3.6.1.3 0 .7-.2 1z"/></svg>
        031 574 19 86</p>
    </div>
    <p class="dish-caption">Kottu Rotti das populärstes<br>Gericht aus SriLanka</p>
    <div class="dish-photo" role="img" aria-label="Foto: Teller mit Kottu Rotti, garniert mit Petersilie, Zitronenhälfte und Zwiebelringen"></div>
  </section>

</main>
</body>
</html>
```